Business Card Design Project

I want a cleaner business card and envelope then what we have now, its too crowded.
Updates

I update with logo, this can be changed anyway you feel it looks best. I also have put gaurantee on there and extended time, this is my first time doing this. Also gave an example of current card

Target Market(s)

a wide array of customers from lattice 700 to small companies and cleints

Industry/Entity Type

Business

Requirements
Must have
• Need to have address, telephone number email
Nice to have
• a sharp professional card that stands out but is still very clean.
Should not have
• Not crazy looking

```html
<!DOCTYPE html>
<html lang="en">
<head>
<meta charset="utf-8">
<title>Halden Assurance Group — Stationery</title>
<link rel="stylesheet" href="https://fonts.googleapis.com/css2?family=Michroma&display=swap">
<style>
  :root {
    --page: #ffffff;
    --charcoal: #454545;
    --ink: #2b2b2b;
    --grey-light: #9a9b98;
    --grey-dark: #55574f;
    --text-light: #f2f2f2;
    --edge: #bdbdbd;
  }
  * { box-sizing: border-box; margin: 0; padding: 0; }
  html, body { width: 1083px; height: 1200px; overflow: hidden; background: var(--page); }
  body { position: relative; font-family: "Michroma", sans-serif; color: var(--ink); }

  .card, .envelope-front, .envelope-flap { position: absolute; }
  .card { width: 288px; height: 164px; border: 1px solid var(--edge); }

  .card-back { left: 410px; top: 180px; background: var(--charcoal); display: flex; align-items: center; justify-content: center; }
  .card-back .web { color: var(--text-light); font-size: 8px; letter-spacing: 0.3px; margin-top: -10px; }

  .card-front { left: 410px; top: 354px; background: var(--page); overflow: hidden; }

  .tone-panel {
    position: absolute; top: 0; bottom: 0; right: 0;
    background: linear-gradient(90deg, var(--grey-light), var(--grey-dark));
  }
  .card-front .tone-panel { left: 132px; }
  .envelope-front .tone-panel { left: 570px; }

  .brand { position: absolute; color: var(--ink); line-height: 1; }
  .brand .mark { display: block; background: var(--grey-dark); }
  .brand .name { display: block; letter-spacing: 1.5px; }
  .brand .sub { display: block; letter-spacing: 0.6px; }

  .card-front .brand { left: 8px; top: 14px; }
  .card-front .mark { width: 24px; height: 24px; margin: 0 0 6px 28px; }
  .card-front .name { font-size: 10.5px; }
  .card-front .sub { font-size: 5px; margin-top: 3px; }

  .contact { position: absolute; right: 12px; bottom: 10px; text-align: right; color: var(--text-light); font-size: 6.2px; line-height: 8.4px; }
  .contact .person { font-size: 7px; }
  .contact .role { font-size: 5.5px; margin-bottom: 7px; }

  .envelope-flap { left: 171px; top: 560px; width: 760px; height: 118px; }
  .envelope-flap svg { position: absolute; inset: 0; width: 100%; height: 100%; }
  .flap-text { position: absolute; left: 0; right: 0; top: 30px; text-align: center; color: var(--text-light); font-size: 9px; line-height: 13px; letter-spacing: 0.4px; }
  .flap-text .web { font-size: 9.5px; }

  .envelope-front { left: 171px; top: 696px; width: 760px; height: 364px; border: 1px solid #7d7d7d; background: var(--page); overflow: hidden; }
  .envelope-front .brand { left: 22px; top: 22px; }
  .envelope-front .mark { width: 50px; height: 50px; margin: 0 0 10px 64px; }
  .envelope-front .name { font-size: 20px; }
  .envelope-front .sub { font-size: 8.5px; margin-top: 4px; }
</style>
</head>
<body>

  <section class="card card-back" aria-label="Business card, back">
    <p class="web">WWW.WEBSITEADDRESS.COM</p>
  </section>

  <section class="card card-front" aria-label="Business card, front">
    <div class="tone-panel" role="img" aria-label="Decorative grey gradient area"></div>
    <div class="brand">
      <span class="mark"></span>
      <span class="name">HALDEN</span>
      <span class="sub">ASSURANCE GROUP</span>
    </div>
    <div class="contact">
      <p class="person">FIRST AND LAST NAME</p>
      <p class="role">title</p>
      <p>STREET INFORMATION</p>
      <p>CITY COUNTRY XXXXXX</p>
      <p>P. 000 000 0000</p>
      <p>F. 000 000 0000</p>
      <p>E. NAME@DOMAIN.COM</p>
    </div>
  </section>

  <section class="envelope-flap" aria-label="Envelope back flap">
    <svg viewBox="0 0 760 118" preserveAspectRatio="none" aria-hidden="true">
      <path d="M0 0 L760 0 L760 70 L720 118 L40 118 L0 70 Z" fill="var(--charcoal)"/>
    </svg>
    <div class="flap-text">
      <p>STREET INFORMATION CITY COUNTRY XXXXXX</p>
      <p>P. 000 000 0000&nbsp;&nbsp;F. 000 000 0000&nbsp;&nbsp;E. NAME@DOMAIN.COM</p>
      <p class="web">WWW.WEBSITEADDRESS.COM</p>
    </div>
  </section>

  <section class="envelope-front" aria-label="Envelope, front">
    <div class="tone-panel" role="img" aria-label="Decorative grey gradient area"></div>
    <div class="brand">
      <span class="mark"></span>
      <span class="name">HALDEN</span>
      <span class="sub">ASSURANCE GROUP</span>
    </div>
  </section>

</body>
</html>
```